Bureau for Venture and Discovery Links Needs a Graphically Designed Powerpoint Template

We are from Bureau for Venture and Discovery Links (BVDL), part of a medical school. BVDL contributes to the medical school by overseeing and managing intellectual property generated by researchers at the medical school, and also works to ensure optimal commercial outcomes for all inventions arising from the medical school. We want a graphically designed powerpoint presentation template to describe how BVDL is involved in a researcher’s journey to major scientific contributions. The journey should be represented in the form of a main road (or pathway). Along the main road, there will be smaller roads branching out, each representing one of the researcher’s major scientific contributions. We will be inputting text details of each major scientific contribution near each of the small road branches. The smaller road branches will also need to be removable / editable. This is because we might need to send the template to different researchers to input details of their major scientific contributions, and each researcher will have a different number of them. Hence, you can possibly place around 6 branches along the main road, but we want to be able to remove the branches should we need to. Removal of the branches (design elements) should still result in a seamless image in powerpoint. We also want to be able to add and edit text in the design template. The start of the main road should contain a placeholder for us to place the researcher’s photo. The end of the road will lead to one of the major scientific contributions. Please see the uploaded sketch to have an idea of what we are looking to get. We welcome deviations and changes to the design as shown from the sketch, as long as the design is able to convey what we have described above. As this powerpoint template will be used for presentation to the senior management, we need it to look beautiful yet professional.

Target Market(s)

Researcher, Scientist

Industry/Entity Type

School

Font styles to use
Serif
Sans Serif

Requirements
Must have
• A main road or pathway as mentioned in the project description.
Nice to have
• We will leave the "nice to haves" to be decided by the designer.
Should not have
• Trees

```html
<!DOCTYPE html>
<html lang="en">
<head>
<meta charset="utf-8">
<title>Researcher Journey – BVDL</title>
<link href="https://fonts.googleapis.com/css2?family=Lato:ital,wght@0,400;0,700;0,900;1,400&display=swap" rel="stylesheet">
<style>
  :root {
    --navy: #2b3a8c;
    --orange: #c1702b;
    --text-grey: #666666;
    --dark-grey: #555555;
    --line-blue: #2f3d91;
    --page: #ffffff;
  }
  * { margin: 0; padding: 0; box-sizing: border-box; }
  html, body {
    width: 1200px; height: 1200px; overflow: hidden;
    background: var(--page);
    font-family: 'Lato', Arial, sans-serif;
  }
  .slide {
    position: absolute; left: 40px; top: 30px;
    width: 1122px; height: 631px;
    background: linear-gradient(180deg, #ffffff 0%, #f4f4f4 45%, #dedede 100%);
    box-shadow: 0 2px 6px rgba(0,0,0,0.35);
    overflow: hidden;
  }
  .slide-title {
    position: absolute; left: 0; right: 0; top: 28px;
    text-align: center; color: var(--navy);
    font-weight: 900; font-size: 42px; letter-spacing: -0.5px;
  }
  .slide-subtitle {
    position: absolute; left: 170px; right: 170px; top: 84px;
    text-align: center; color: var(--text-grey);
    font-style: italic; font-size: 17.5px; line-height: 23px;
  }
  .journey-map { position: absolute; left: 0; top: 0; width: 1122px; height: 631px; }
  .researcher-photo {
    position: absolute; left: 71px; top: 168px; width: 124px; height: 124px;
    border-radius: 50%;
    background: radial-gradient(circle at 50% 35%, #e9d3c4 0 18%, #2a2a2a 19% 22%, #f2f2f2 23% 55%, #2c2c30 56%);
    border: 2px solid #ffffff;
    box-shadow: 0 2px 6px rgba(0,0,0,0.25);
  }
  .researcher-name {
    position: absolute; left: 40px; width: 186px; top: 296px;
    text-align: center; color: var(--dark-grey); font-weight: 700; font-size: 12px;
  }
  .researcher-role {
    position: absolute; left: 40px; width: 186px; top: 312px;
    text-align: center; color: var(--text-grey); font-size: 10.5px;
  }
  .award-box {
    position: absolute; left: 51px; top: 339px; width: 163px; height: 142px;
    background: var(--navy); color: #fff; text-align: center;
    padding: 12px 10px; box-shadow: 2px 3px 5px rgba(0,0,0,0.35);
  }
  .award-box h3 { font-weight: 700; font-size: 12px; margin-bottom: 9px; }
  .award-box p { font-size: 9px; line-height: 11.2px; }
  .contribution-box {
    position: absolute; left: 865px; top: 351px; width: 208px; height: 245px;
    background: var(--orange); color: #fff; text-align: center;
    padding: 24px 14px 0; box-shadow: 2px 3px 5px rgba(0,0,0,0.35);
  }
  .contribution-box h3 { font-weight: 700; font-size: 14.5px; line-height: 17px; margin-bottom: 12px; }
  .contribution-box p { font-size: 11px; line-height: 14px; }
  .contribution-box svg { display: block; margin: 22px auto 0; }
  .milestone { position: absolute; }
  .milestone h4 { color: var(--navy); font-weight: 900; font-size: 14.5px; margin-bottom: 5px; }
  .milestone p {
    color: var(--text-grey); font-size: 9.1px; line-height: 11.2px; text-align: justify;
  }
  .milestone.align-right h4 { text-align: right; }
  .m1 { left: 409px; top: 176px; width: 143px; }
  .m2 { left: 252px; top: 350px; width: 115px; }
  .m3 { left: 280px; top: 470px; width: 116px; }
  .m4 { left: 630px; top: 218px; width: 101px; }
  .m5 { left: 442px; top: 527px; width: 116px; }
  .m6 { left: 705px; top: 367px; width: 100px; }
</style>
</head>
<body>
<div class="slide">
  <h1 class="slide-title">LOREM IPSUM DOLOR SIT AMET</h1>
  <p class="slide-subtitle">Lorem ipsum dolor sit amet, consetetur sadipscing elitr, sed diam nonumy eirmod tempor invidunt ut labore et dolore magna aliquyam erat, sed diam voluptua. At vero eos et</p>

  <svg class="journey-map" viewBox="50 38 1402 788" aria-hidden="true">
    <defs>
      <linearGradient id="roadFill" x1="0" y1="0" x2="1" y2="0.3">
        <stop offset="0" stop-color="#e6e6e6"/>
        <stop offset="0.45" stop-color="#b9b9b9"/>
        <stop offset="1" stop-color="#8c8c8c"/>
      </linearGradient>
      <marker id="arrowHead" viewBox="0 0 10 10" refX="9" refY="5" markerWidth="6" markerHeight="6" orient="auto-start-reverse">
        <path d="M0,0 L10,5 L0,10 Z" fill="var(--line-blue)"/>
      </marker>
    </defs>
    <path class="main-road" fill="url(#roadFill)"
      d="M290,355 C450,372 650,430 722,505 C740,528 735,548 722,560 C710,572 712,580 722,590
         C770,650 900,700 1095,712 L1085,708 L1168,752 L1040,772 L1062,752
         C880,742 700,690 660,600 C648,572 660,556 678,538 C630,462 450,402 270,390 Z"/>
    <g class="branches" fill="none" stroke="var(--line-blue)" stroke-width="1.3">
      <polyline points="438,400 438,279 543,279" marker-end="url(#arrowHead)"/>
      <polyline points="558,430 558,486 520,486" marker-end="url(#arrowHead)"/>
      <polyline points="632,470 632,640 561,640" marker-end="url(#arrowHead)"/>
      <polyline points="693,494 693,388 822,388" marker-end="url(#arrowHead)"/>
      <polyline points="800,676 800,708 761,708" marker-end="url(#arrowHead)"/>
      <polyline points="878,690 878,521 915,521" marker-end="url(#arrowHead)"/>
    </g>
    <g class="branch-dots" fill="var(--line-blue)">
      <circle cx="438" cy="400" r="4"/><circle cx="558" cy="430" r="4"/>
      <circle cx="632" cy="470" r="4"/><circle cx="693" cy="494" r="4"/>
      <circle cx="800" cy="676" r="4"/><circle cx="878" cy="690" r="4"/>
    </g>
  </svg>

  <div class="researcher-photo" role="img" aria-label="Portrait photo of the researcher"></div>
  <p class="researcher-name">MD. Ph. Dr. Lorem impsum</p>
  <p class="researcher-role">Lorem ipsum dolor sit amet</p>

  <div class="award-box">
    <h3>STAR AWARD</h3>
    <p>Lorem ipsum dolor sit amet, consetetur sadipscing elitr, sed diam nonumy eirmod tempor invidunt ut labore et dolore magna aliquyam erat, sed diam voluptua. At vero eos et accusam et justo duo dolores et ea rebum.</p>
  </div>

  <div class="milestone m1"><h4>LOREM IPSUM</h4><p>Lorem ipsum dolor sit amet, consetetur sadipscing elitr, sed diam nonumy eirmod tempor invidunt ut labore et dolore magna aliquyam erat, sed diam voluptua.</p></div>
  <div class="milestone m2 align-right"><h4>LOREM IPSUM</h4><p>Lorem ipsum dolor sit amet, consetetur sadipscing elitr, sed diam nonumy eirmod tempor invidunt ut labore et dolore magna aliquyam erat, sed diam voluptua.</p></div>
  <div class="milestone m3 align-right"><h4>LOREM IPSUM</h4><p>Lorem ipsum dolor sit amet, consetetur sadipscing elitr, sed diam nonumy eirmod tempor invidunt ut labore et dolore magna aliquyam erat, sed diam voluptua.</p></div>
  <div class="milestone m4"><h4>LOREM IPSUM</h4><p>Lorem ipsum dolor sit amet, consetetur sadipscing elitr, sed diam nonumy eirmod tempor invidunt ut labore et dolore magna aliquyam erat, sed diam voluptua.</p></div>
  <div class="milestone m5 align-right"><h4>LOREM IPSUM</h4><p>Lorem ipsum dolor sit amet, consetetur sadipscing elitr, sed diam nonumy eirmod tempor invidunt ut labore et dolore magna aliquyam erat, sed diam voluptua.</p></div>
  <div class="milestone m6"><h4>LOREM IPSUM</h4><p>Lorem ipsum dolor sit amet, consetetur sadipscing elitr, sed diam nonumy eirmod tempor invidunt ut labore et dolore magna aliquyam erat, sed diam voluptua.</p></div>

  <div class="contribution-box">
    <h3>MAJOR SCIENTIFIC<br>CONTRIBUTION</h3>
    <p>Lorem ipsum dolor sit amet, consetetur sadipscing elitr, sed diam nonumy eirmod tempor invidunt ut labore et dolore magna aliquyam erat, sed diam voluptua.</p>
    <svg width="56" height="54" viewBox="0 0 56 54" aria-hidden="true">
      <path d="M2,2 H42 L50,10 V36 H2 Z" fill="#ffffff"/>
      <g stroke="var(--orange)" stroke-width="2.5">
        <line x1="8" y1="11" x2="30" y2="11"/><line x1="8" y1="18" x2="34" y2="18"/><line x1="8" y1="25" x2="26" y2="25"/>
      </g>
      <path d="M36,44 L32,53 L38,50 L40,44 Z M46,44 L50,53 L44,50 L42,44 Z" fill="#ffffff"/>
      <circle cx="41" cy="38" r="9" fill="#ffffff" stroke="var(--orange)" stroke-width="2"/>
      <circle cx="41" cy="38" r="4" fill="none" stroke="var(--orange)" stroke-width="1.5"/>
    </svg>
  </div>
</div>
</body>
</html>
```